Flyer Design - Child Care Centre

I need a flyer design (d/sided), full colour for a Child Care Centre that I have recently bought. Check out my website (tiny-sprouts.com.au) for information on what we do, our services, philosophy, fees and hours of operation.

The purpose of this flyer is to advertise our services as a child care centre (under new management) to the local community and with various hospitals.

The flyer should embody our philosophy, the text on my home page (particularly our QX focus) and some of the parent testimonials. It should also include my logo and Zibb (refer attached AI and jpeg files, eps available on request).

Feel free to add stock photo's of kids and cartoon characters and use the following CMYK colours if incorporating any coloured text. Green: C-78, M-0, Y-100, K-0 Magenta: C-0, M-100, Y-33, K-10

```html
<!DOCTYPE html>
<html lang="en">
<head>
<meta charset="utf-8">
<title>Tiny Sprouts Child Care – Flyer Back</title>
<link href="https://fonts.googleapis.com/css2?family=Delius&family=Fredoka:wght@400;600&family=Open+Sans:wght@400;600&display=swap" rel="stylesheet">
<style>
:root{
  --green:#2bb24c;
  --magenta:#d6115f;
  --ink:#1a1a1a;
  --paper:#ffffff;
  --stage:#e6e6e6;
  --photo-warm:#c9a88a;
  --photo-grey:#bdbab3;
}
*{box-sizing:border-box;margin:0;padding:0}
html,body{width:1200px;height:1000px;overflow:hidden;background:var(--stage)}
.flyer{position:absolute;left:274px;top:41px;width:652px;height:917px;background:var(--paper);font-family:"Delius",cursive;color:var(--ink);box-shadow:0 2px 10px rgba(0,0,0,.25)}
.top-band{position:absolute;left:0;top:0;width:100%;height:13px;background:var(--green)}
.intro{position:absolute;left:17px;top:18px;width:353px;font-size:15px;line-height:24.5px;text-align:justify}
.intro p{margin-bottom:3px}
.intro .we{color:var(--magenta)}
.services{position:absolute;left:15px;top:245px;width:620px;font-size:15px;line-height:24px;text-align:justify}
.services .name{color:var(--magenta)}
.photo{position:absolute;border:2px solid var(--magenta);box-shadow:0 1px 4px rgba(0,0,0,.3)}
.photo-sleeping{left:382px;top:29px;width:251px;height:195px;background:linear-gradient(135deg,#d9d6cf,var(--photo-grey) 55%,#6f83a0)}
.photo-melon{left:358px;top:548px;width:268px;height:168px;background:linear-gradient(120deg,#d8463f,#c99878 45%,#3f6e2a)}
.panel{position:absolute;top:305px;width:290px;height:180px}
.panel-philosophy{left:24px}
.panel-goals{left:337px}
.panel .ribbon{position:absolute;left:0;top:0;width:100%;height:36px;font-family:"Fredoka",sans-serif;font-size:22px;text-align:center;line-height:38px;color:var(--ink);box-shadow:0 2px 3px rgba(0,0,0,.25)}
.panel-philosophy .ribbon{background:var(--green)}
.panel-goals .ribbon{background:var(--magenta)}
.panel .card{position:absolute;left:8px;right:8px;top:36px;bottom:0;background:var(--paper);box-shadow:0 1px 4px rgba(0,0,0,.35);padding:12px 10px 8px;font-size:9.6px;line-height:11px;text-align:justify}
.panel .card p{margin-bottom:10px}
.panel-philosophy .card{color:var(--magenta)}
.panel-goals .card{color:var(--green);font-size:8px;line-height:9.4px}
.fees-title{position:absolute;left:15px;top:499px;width:265px;height:40px;border:2px dashed var(--green);font-family:"Fredoka",sans-serif;font-weight:600;font-size:28px;color:var(--magenta);line-height:38px;padding-left:10px}
.fees{position:absolute;left:30px;top:550px;width:308px;border-collapse:collapse;background:var(--green);box-shadow:0 1px 4px rgba(0,0,0,.35);font-family:"Open Sans",sans-serif;font-size:15px;color:#fff}
.fees td{height:27.3px;border:1px solid #fff;padding:0 12px;white-space:nowrap}
.fees td.price{padding:0 4px;width:116px}
.notes{position:absolute;left:19px;top:720px;width:620px;font-family:"Open Sans",sans-serif;font-size:11px;line-height:15px;list-style:none}
.notes li{padding-left:8px;text-indent:-8px}
.notes li::before{content:"● ";font-size:8px}
.contact{position:absolute;left:0;bottom:0;width:100%;height:147px;background:var(--magenta);color:#fff;font-family:"Open Sans",sans-serif}
.contact h2{position:absolute;left:20px;top:10px;font-family:"Fredoka",sans-serif;font-weight:600;font-size:26px;border-bottom:1px solid #fff;padding-bottom:1px;line-height:30px}
.contact .line{position:absolute;display:flex;align-items:center;gap:12px}
.contact svg{flex:none}
.phone{left:22px;top:64px;font-size:24px}
.email{left:22px;top:102px;font-size:16px}
.web{left:22px;top:126px;font-size:16px;display:none}
.divider{position:absolute;left:358px;top:15px;width:2px;height:95px;background:#fff}
.social{left:370px;font-size:16px;gap:8px}
.social .dot{width:14px;height:14px;border-radius:50%;background:#fff}
.social-a{top:20px}
.social-b{top:56px}
.address{position:absolute;left:368px;top:92px;font-size:16px;line-height:23px}
</style>
</head>
<body>
<main class="flyer">
  <div class="top-band"></div>

  <section class="intro">
    <p><span class="we">We</span> provide a child care environment that enhances the emotional and physical health of your child, stimulates the children’s involvement in activities and encourages self-esteem and a sense of achievement.</p>
    <p><span class="we">We</span> encourage all families to visit our centre regularly so as to experience and engage in our positive and relaxing atmosphere and to meet and interact with our educators.</p>
  </section>
  <div class="photo photo-sleeping" role="img" aria-label="Photo of a toddler in denim overalls asleep on a pale sheet beside a flower"></div>

  <p class="services"><span class="name">Tiny Sprouts child care centre</span> – Long Day Care, Before &amp; After School Care (Schoolies/OSHC) and Vacation Care for children.</p>

  <section class="panel panel-philosophy">
    <h3 class="ribbon">Our Philosophy</h3>
    <div class="card">
      <p>Every child is unique and we believe that success and growth comes from learning with encouragement and praise.</p>
      <p>Our educator’s focus on building every child’s self esteem and confidence through positive feedback, We nurture their natural strengths.</p>
      <p>A child sees the world around them with wonder and awe, we believe in encouraging their natural curiosity.</p>
    </div>
  </section>

  <section class="panel panel-goals">
    <h3 class="ribbon">Our Goals</h3>
    <div class="card">
      <p>We act as an extension of the home. We strive to provide an environment where children feel loved, accepted and secure. We foster strong partnerships with home, creating a smooth and caring transition between the home and the Centre. Parents participation is encouraged and educators work in consultation with parents.</p>
      <p>Children are encouraged to achieve their best socially, emotionally and academically. We listen to their voices. We recognise our moral and social obligation to our children, their families and the greater community providing the children with a core foundation that will support them through life towards becoming active members of the community.</p>
    </div>
  </section>

  <h2 class="fees-title">Our Fees &amp; Hours</h2>
  <table class="fees">
    <tr><td>BABIES (0-2YRS)</td><td class="price">$85.00 PER DAY</td></tr>
    <tr><td>TODDLERS (2-3YRS)</td><td class="price">$85.00 PER DAY</td></tr>
    <tr><td>KINDY (3-6YRS)</td><td class="price">$85.00 PER DAY</td></tr>
    <tr><td>BEFORE SCHOOL</td><td class="price">$25.00 PER DAY</td></tr>
    <tr><td>AFTER SCHOOL</td><td class="price">$28.00 PER DAY</td></tr>
    <tr><td>*VACATION CARE</td><td class="price">$85.00 PER DAY</td></tr>
  </table>
  <div class="photo photo-melon" role="img" aria-label="Photo of a smiling child eating a slice of watermelon on a grass background"></div>

  <ul class="notes">
    <li>Fees are payable two weeks in advance via direct debit.</li>
    <li>*Please note that Vacation Care does not include excursions. We create a vacation care plan to be affordable e.g. only 2 paying excursions per week.</li>
  </ul>

  <footer class="contact">
    <h2>For More Information :</h2>
    <div class="line phone">
      <svg width="24" height="20" viewBox="0 0 24 20" aria-hidden="true"><path d="M2 7c0-3 4-5 10-5s10 2 10 5v2h-5V7H7v2H2z" fill="#fff"/><rect x="5" y="10" width="14" height="9" rx="1" fill="#fff"/><circle cx="12" cy="14.5" r="2.5" fill="var(--magenta)"/></svg>
      <span>(08) 9000 4127</span>
    </div>
    <div class="line email">
      <svg width="24" height="16" viewBox="0 0 24 16" aria-hidden="true"><rect x="1" y="1" width="20" height="13" fill="none" stroke="#fff" stroke-width="1.6"/><path d="M1 1l10 7 10-7" fill="none" stroke="#fff" stroke-width="1.6"/></svg>
      <span>enquiries@tiny-sprouts.com.au</span>
    </div>
    <div class="line" style="left:22px;top:126px;font-size:16px">
      <svg width="24" height="22" viewBox="0 0 24 22" aria-hidden="true"><circle cx="10" cy="10" r="8" fill="none" stroke="#fff" stroke-width="1.6"/><ellipse cx="10" cy="10" rx="3.5" ry="8" fill="none" stroke="#fff" stroke-width="1.2"/><path d="M2 10h16M3.5 6h13M3.5 14h13" stroke="#fff" stroke-width="1.1"/><path d="M17 17l5 4" stroke="#fff" stroke-width="2.4"/></svg>
      <span>www.tiny-sprouts.com.au</span>
    </div>
    <div class="divider"></div>
    <div class="line social social-a"><span class="dot"></span><span>@ tinysproutsOZ</span></div>
    <div class="line social social-b"><span class="dot"></span><span>@TinySproutsAU</span></div>
    <p class="address">18 Wattle Road, Banksia Vale,<br>Western Australia 6000</p>
  </footer>
</main>
</body>
</html>
```